BrivoPeak Business Card Design Project

We are looking for a modern, clean business card design for our new company. We are a consulting firm focused on the financial services market providing management and IT consulting to banks, insurance companies, etc. Please include our company logo and company contact information from the attached file in the design. Two versions of the logo are attached, either version is acceptable. Logos are available in other file formats if needed. We would like to include the contact information for both our UK and US offices as well as the following information for each individual card holder: Name, position/title, address, phone number and e-mail address.
Updates
Project Deadline Extended
Reason: A last minute trip over seas has prevented us from finalizing the decision. A decision will be made this week. We apologize for the inconvenience.
Industry/Entity Type
Business
Contact Information for Business Card
Company logo.
Company locations and phone numbers for both the US and UK offices.
Company URL.
Cardholder Name
Cardholder Position/title
Cardholder Address
Cardholder Phone Number
Cardholder e-mail Address
Look and feel
Each slider illustrates characteristics of the customer's brand and the style your logo design should communicate.

```html
<!DOCTYPE html>
<html lang="en">
<head>
<meta charset="utf-8">
<title>BrivoPeak Partners – Business Cards</title>
<link href="https://fonts.googleapis.com/css2?family=Open+Sans:wght@400;700&display=swap" rel="stylesheet">
<style>
  :root {
    --bg-light: #0e8fd0;
    --bg-dark: #0a6896;
    --card: #ffffff;
    --band: #1f80a6;
    --navy: #1c3157;
    --ink: #1a1a1a;
    --flag-uk: #2a3f7a;
    --flag-us: #b8434f;
  }
  * { margin: 0; padding: 0; box-sizing: border-box; }
  html, body { width: 1200px; height: 1000px; overflow: hidden; }
  body {
    position: relative;
    font-family: "Open Sans", Arial, sans-serif;
    background: radial-gradient(ellipse at 20% 50%, var(--bg-light), var(--bg-dark));
    color: var(--ink);
  }
  .card {
    position: absolute;
    left: 345px;
    width: 511px;
    height: 283px;
    background: var(--card);
  }
  .card--front { top: 194px; }
  .card--back { top: 520px; }

  .brand {
    position: absolute;
    display: flex;
    align-items: center;
    gap: 8px;
    font-weight: 700;
    color: var(--navy);
    white-space: nowrap;
  }
  .brand__mark { width: 12px; height: 12px; background: var(--navy); }
  .card--front .brand { top: 40px; left: 0; right: 0; justify-content: center; font-size: 22px; }
  .card--back .brand { top: 126px; left: 24px; font-size: 24px; flex-direction: column; align-items: center; gap: 6px; }
  .card--back .brand__mark { width: 16px; height: 16px; }

  .holder-band {
    position: absolute;
    top: 104px; left: 0; right: 0;
    height: 100px;
    background: var(--band);
    color: #fff;
    text-align: center;
    font-size: 14px;
  }
  .holder-band .holder-name { font-size: 15px; margin-top: 10px; }
  .holder-band p { margin-top: 11px; }

  .footer-link {
    position: absolute;
    bottom: 20px;
    font-size: 13px;
  }
  .footer-link--left { left: 24px; }
  .footer-link--right { right: 24px; }
  .card--back .footer-link { bottom: 20px; }

  .office { position: absolute; left: 258px; font-size: 14px; line-height: 19.5px; }
  .office--uk { top: 20px; }
  .office--us { top: 125px; }
  .office__phone { display: flex; align-items: center; gap: 4px; margin-left: -2px; }
  .flag { width: 22px; height: 12px; display: inline-block; }
  .flag--uk { background: var(--flag-uk); }
  .flag--us { background: linear-gradient(var(--flag-us) 50%, #e8e8f0 50%); }
  .office__address { margin-left: 24px; margin-top: 7px; }
</style>
</head>
<body>
  <section class="card card--front">
    <div class="brand"><span class="brand__mark"></span>BrivoPeak Partners</div>
    <div class="holder-band">
      <p class="holder-name">Sam Rowe - Manager</p>
      <p>0044 55501234</p>
      <p>12 Example Road 10101</p>
    </div>
    <span class="footer-link footer-link--left">www.brivopeakpartners.com</span>
    <span class="footer-link footer-link--right">info@www.brivopeakpartners.com</span>
  </section>

  <section class="card card--back">
    <div class="brand"><span class="brand__mark"></span>BrivoPeak Partners</div>
    <div class="office office--uk">
      <div class="office__phone"><span class="flag flag--uk" role="img" aria-label="United Kingdom flag"></span>+44 7700 900461</div>
      <div class="office__address">14 Harrow Lane<br>London E2 8QT<br>Great Britain</div>
    </div>
    <div class="office office--us">
      <div class="office__phone"><span class="flag flag--us" role="img" aria-label="United States flag"></span>(555) 014-2297</div>
      <div class="office__address">512 N Cedar Ave Suite 204-118<br>Maplewood UT 84990<br>United States</div>
    </div>
    <span class="footer-link footer-link--left">info@www.brivopeakpartners.com</span>
    <span class="footer-link footer-link--right">www.brivopeakpartners.com</span>
  </section>
</body>
</html>
```